RZO Design tag

Looking to design a tag for our new hat & glove brand RZO Design. These are winter hats & gloves. Long story short these are lower cost/retail items but I'm trying to convey higher quality goods through a nice tag. I’ve attached a tag of another brand we have to give you a general idea of what I’d be looking for- but again for our new brand RZO Design.
I’m thinking we can do one general design- and then do it in 4 different color schemes: First one mimicking the attachment’s colors for ladies items- so a few different shades of pink. Then 2nd color scheme a darker more masculine color tone for mens or unisex items- maybe blue/dark blue, and then a 3rd color scheme for kids items that is more vibrant/kid like colors. Last one red & green for some Christmas items we do.
A few things:
• Trying to make the tags look classy as possible
• The tag will need to measure 2.25” high x 2” wide. The top little bit would have to be space left blank for a hole punch- just like on the attached sample tag. But again the tags designed would need to be 2.25" tall x 2" wide so not the same shape as the sample tag.
• For item name you can just put “Knit Hat” for the generic tag item name (in place of what says on the same “Chenille Slipper Bootie”). Please try to keep the writing a nice font similar to what is on this tag- again trying to have a classy tag look
• On the bottom center (In place of Made in China) it would just need to say “One Size” in standard font
Hope this helps & thank you
Target Market(s)
People buying winter hats & gloves
Industry/Entity Type
Retail- winter hats & gloves
Look and feel

```html
<!DOCTYPE html>
<html lang="en">
<head>
<meta charset="utf-8">
<title>RZO Design – Knit Hat Tags</title>
<link rel="stylesheet" href="https://fonts.googleapis.com/css2?family=Allura&family=Montserrat:wght@600;700&display=swap">
<style>
  :root {
    --backdrop: #e4e4e4;
    --ink: #ffffff;
    --eyelet-ring: #f4f4f4;
    --eyelet-hole: #cfcfcf;

    --ladies-base: #e48bbd;
    --ladies-deep: #c95a9b;
    --ladies-accent: #b8337f;

    --mens-base: #2aa6de;
    --mens-deep: #1f84c4;
    --mens-accent: #2b3990;

    --kids-base: #8dd14a;
    --kids-deep: #3fb3a8;
    --kids-accent: #f7941d;

    --holiday-base: #ea2129;
    --holiday-deep: #c51b24;
    --holiday-accent: #2f9e48;
  }

  * { box-sizing: border-box; margin: 0; padding: 0; }

  html, body {
    width: 1200px;
    height: 619px;
    overflow: hidden;
    background: var(--backdrop);
  }

  .tag-row {
    display: flex;
    gap: 40px;
    justify-content: center;
    align-items: center;
    width: 1200px;
    height: 619px;
  }

  /* 2" wide × 2.25" tall */
  .tag {
    position: relative;
    flex: 0 0 auto;
    width: 250px;
    height: 281px;
    overflow: hidden;
    color: var(--ink);
  }

  .tag__pattern {
    position: absolute;
    inset: 0;
    background: linear-gradient(135deg, var(--base) 0%, var(--deep) 55%, var(--base) 100%);
  }

  .tag--ladies  { --base: var(--ladies-base);  --deep: var(--ladies-deep);  --accent: var(--ladies-accent); }
  .tag--mens    { --base: var(--mens-base);    --deep: var(--mens-deep);    --accent: var(--mens-accent); }
  .tag--kids    { --base: var(--kids-base);    --deep: var(--kids-deep);    --accent: var(--kids-accent); }
  .tag--holiday { --base: var(--holiday-base); --deep: var(--holiday-deep); --accent: var(--holiday-accent); }

  .tag__eyelet {
    position: absolute;
    top: 12px;
    left: 50%;
    transform: translateX(-50%);
  }

  .tag__brand {
    position: absolute;
    top: 66px;
    left: 0;
    right: 0;
    display: flex;
    justify-content: center;
    align-items: center;
    gap: 8px;
  }

  .tag__brand-mark {
    width: 16px;
    height: 16px;
    background: var(--accent);
  }

  .tag__brand-name {
    font-family: "Montserrat", sans-serif;
    font-weight: 700;
    font-size: 21px;
    letter-spacing: 0.12em;
    text-transform: uppercase;
    color: var(--ink);
  }

  .tag__item {
    position: absolute;
    top: 134px;
    left: 0;
    right: 0;
    text-align: center;
    font-family: "Allura", cursive;
    font-size: 54px;
    line-height: 1;
    color: var(--ink);
  }

  .tag__size {
    position: absolute;
    bottom: 18px;
    left: 0;
    right: 0;
    text-align: center;
    font-family: "Montserrat", sans-serif;
    font-weight: 700;
    font-size: 11px;
    letter-spacing: 0.04em;
    text-transform: uppercase;
    color: var(--ink);
  }
</style>
</head>
<body>
  <main class="tag-row">

    <article class="tag tag--ladies">
      <div class="tag__pattern" role="img" aria-label="Pink interlocking chevron pattern"></div>
      <svg class="tag__eyelet" width="22" height="22" viewBox="0 0 24 24" aria-hidden="true">
        <circle cx="12" cy="12" r="11" fill="var(--eyelet-ring)"/>
        <circle cx="12" cy="12" r="6" fill="var(--eyelet-hole)"/>
      </svg>
      <div class="tag__brand">
        <span class="tag__brand-mark"></span>
        <span class="tag__brand-name">RZO Design</span>
      </div>
      <p class="tag__item">Knit Hat</p>
      <p class="tag__size">One Size</p>
    </article>

    <article class="tag tag--mens">
      <div class="tag__pattern" role="img" aria-label="Blue interlocking chevron pattern"></div>
      <svg class="tag__eyelet" width="22" height="22" viewBox="0 0 24 24" aria-hidden="true">
        <circle cx="12" cy="12" r="11" fill="var(--eyelet-ring)"/>
        <circle cx="12" cy="12" r="6" fill="var(--eyelet-hole)"/>
      </svg>
      <div class="tag__brand">
        <span class="tag__brand-mark"></span>
        <span class="tag__brand-name">RZO Design</span>
      </div>
      <p class="tag__item">Knit Hat</p>
      <p class="tag__size">One Size</p>
    </article>

    <article class="tag tag--kids">
      <div class="tag__pattern" role="img" aria-label="Bright lime and turquoise interlocking chevron pattern"></div>
      <svg class="tag__eyelet" width="22" height="22" viewBox="0 0 24 24" aria-hidden="true">
        <circle cx="12" cy="12" r="11" fill="var(--eyelet-ring)"/>
        <circle cx="12" cy="12" r="6" fill="var(--eyelet-hole)"/>
      </svg>
      <div class="tag__brand">
        <span class="tag__brand-mark"></span>
        <span class="tag__brand-name">RZO Design</span>
      </div>
      <p class="tag__item">Knit Hat</p>
      <p class="tag__size">One Size</p>
    </article>

    <article class="tag tag--holiday">
      <div class="tag__pattern" role="img" aria-label="Red interlocking chevron pattern"></div>
      <svg class="tag__eyelet" width="22" height="22" viewBox="0 0 24 24" aria-hidden="true">
        <circle cx="12" cy="12" r="11" fill="var(--eyelet-ring)"/>
        <circle cx="12" cy="12" r="6" fill="var(--eyelet-hole)"/>
      </svg>
      <div class="tag__brand">
        <span class="tag__brand-mark"></span>
        <span class="tag__brand-name">RZO Design</span>
      </div>
      <p class="tag__item">Knit Hat</p>
      <p class="tag__size">One Size</p>
    </article>

  </main>
</body>
</html>
```